2022 Grenache Hillside Vineyard Sketch Wine Label

Size:4"X4"
Wine: 2022 Grenache
Vineyard Name: Low Mill Vineyard
AVA: Solano County
Alcohol by Volume:15%
Volume:750ml
Must Feature a hillside vineyard on the label somehow, I picture it being a sketch but it doesn't have to be. Not looking for anything flashy or colorful but maybe a pop of color somewhere. I am not yet sure that I want to include our name, but you can try to work in "KMT" somewhere on the label if it fits the design.
The Label must include all the information listed above. The Grenache was grown in a hillside vineyard, so I wanted the label to prominently feature a hillside vineyard. You can layout the label however you see best, but the vintage and varietal should be prominent, the ABV can be in small type face but must be legible following FQD guidelines. If you are able to make the vineyard name pop as well that would be good.
You don't have to use these, but our standard fonts we use are:
For Varietal: Bianca
Secondary (vintage, AVA, Vineyard):Helvetica
ABV/Volume: PT Serif
Thank you, look forward to the results

```html
<!DOCTYPE html>
<html lang="en">
<head>
<meta charset="UTF-8">
<title>Grenache 2022 – Low Mill Vineyard Label</title>
<link href="https://fonts.googleapis.com/css2?family=Sacramento&family=Cinzel:wght@400;600&family=PT+Serif&display=swap" rel="stylesheet">
<style>
  :root {
    --backdrop: #2b2927;
    --paper: #f5f4f2;
    --gold: #c9a24a;
    --ink: #161616;
    --ink-soft: #4a4a4a;
    --sketch-light: #e9e9e9;
    --sketch-mid: #bdbdbd;
  }
  * { margin: 0; padding: 0; box-sizing: border-box; }
  html, body {
    width: 1200px;
    height: 800px;
    overflow: hidden;
    background: var(--backdrop);
  }
  .canvas {
    position: relative;
    width: 1200px;
    height: 800px;
    display: flex;
    align-items: center;
    justify-content: center;
  }
  .label {
    position: relative;
    width: 680px;
    height: 680px;
    background: var(--paper);
    overflow: hidden;
  }
  .label__frame {
    position: absolute;
    inset: 18px;
    border: 3px solid var(--gold);
    pointer-events: none;
  }
  .brand-mark {
    position: absolute;
    top: 34px;
    left: 50%;
    transform: translateX(-50%);
    width: 78px;
    height: 56px;
    background: var(--ink);
    border: 3px solid var(--gold);
    display: flex;
    align-items: center;
    justify-content: center;
    color: var(--paper);
    font-family: "Cinzel", serif;
    font-weight: 400;
    font-size: 20px;
    letter-spacing: 1px;
  }
  .varietal {
    position: absolute;
    top: 108px;
    left: 40px;
    right: 40px;
    text-align: center;
    white-space: nowrap;
    font-family: "Sacramento", cursive;
    font-weight: 400;
    font-size: 150px;
    line-height: 1;
    color: var(--ink);
  }
  .vintage {
    position: absolute;
    top: 240px;
    left: 0;
    right: 0;
    text-align: center;
    font-family: "Cinzel", serif;
    font-size: 28px;
    letter-spacing: 12px;
    padding-left: 12px;
    color: var(--ink);
  }
  .vineyard-name {
    position: absolute;
    top: 360px;
    left: 0;
    right: 0;
    text-align: center;
    font-family: "Cinzel", serif;
    font-weight: 600;
    font-size: 28px;
    letter-spacing: 1px;
    color: var(--ink);
  }
  .divider {
    position: absolute;
    top: 400px;
    left: 50%;
    transform: translateX(-50%);
    width: 300px;
    height: 12px;
  }
  .ava {
    position: absolute;
    top: 416px;
    left: 0;
    right: 0;
    text-align: center;
    font-family: "Cinzel", serif;
    font-size: 22px;
    letter-spacing: 4px;
    color: var(--ink);
  }
  .bottle-facts {
    position: absolute;
    top: 462px;
    left: 0;
    right: 0;
    text-align: center;
    font-family: "PT Serif", serif;
    font-size: 15px;
    letter-spacing: 1px;
    color: var(--ink-soft);
  }
  .hillside-sketch {
    position: absolute;
    left: 21px;
    right: 21px;
    bottom: 21px;
    height: 160px;
    background: linear-gradient(180deg, var(--paper) 0%, var(--sketch-light) 35%, var(--sketch-mid) 100%);
  }
</style>
</head>
<body>
  <main class="canvas">
    <section class="label">
      <div class="hillside-sketch" role="img" aria-label="Pen sketch of a hillside vineyard with rows of vines running toward distant hills"></div>
      <div class="label__frame"></div>
      <div class="brand-mark">KMT</div>
      <h1 class="varietal">Grenache</h1>
      <p class="vintage">2022</p>
      <h2 class="vineyard-name">LOW MILL VINEYARD</h2>
      <svg class="divider" viewBox="0 0 300 12" aria-hidden="true">
        <line x1="10" y1="6" x2="136" y2="6" stroke="#4a4a4a" stroke-width="1.2"/>
        <line x1="164" y1="6" x2="290" y2="6" stroke="#4a4a4a" stroke-width="1.2"/>
        <polyline points="16,2 10,6 16,10" fill="none" stroke="#4a4a4a" stroke-width="1.2"/>
        <polyline points="284,2 290,6 284,10" fill="none" stroke="#4a4a4a" stroke-width="1.2"/>
        <circle cx="150" cy="6" r="3" fill="#4a4a4a"/>
      </svg>
      <p class="ava">SOLANO COUNTY</p>
      <p class="bottle-facts">15% | 750ML</p>
    </section>
  </main>
</body>
</html>
```